Tall Oak Circle.. a non profit that seeks to stomp out skin cancer .. smalls steps toward making big

Simple letterhead incorporating logo

Industry/Entity Type

Non Profit

Font styles to use
Sans Serif

Colors

Designer to choose colors to be used in the design.

```html
<!DOCTYPE html>
<html lang="en">
<head>
<meta charset="utf-8">
<title>Tall Oak Circle — Letterhead</title>
<link rel="stylesheet" href="https://fonts.googleapis.com/css2?family=Nunito:wght@400;800&family=Source+Sans+3:wght@400&display=swap">
<style>
  :root {
    --navy: #1f2544;
    --ink: #1c1f33;
    --paper: #ffffff;
  }
  * { margin: 0; padding: 0; box-sizing: border-box; }
  html, body {
    width: 936px;
    height: 1200px;
    overflow: hidden;
    background: var(--paper);
  }
  .letterhead {
    position: relative;
    width: 936px;
    height: 1200px;
    background: var(--paper);
    color: var(--ink);
    font-family: "Source Sans 3", sans-serif;
  }
  .header-curve {
    position: absolute;
    left: 0;
    top: 0;
    width: 936px;
    height: 260px;
  }
  .brand-mark {
    position: absolute;
    left: 91px;
    top: 25px;
    width: 164px;
    height: 164px;
    border-radius: 50%;
    background: var(--navy);
  }
  .brand-name {
    position: absolute;
    left: 293px;
    top: 60px;
    font-family: "Nunito", sans-serif;
    font-weight: 800;
    font-size: 34px;
    letter-spacing: 3.5px;
    color: var(--navy);
    line-height: 1;
  }
  .brand-contact {
    position: absolute;
    left: 294px;
    top: 104px;
    font-family: "Nunito", sans-serif;
    font-weight: 400;
    font-size: 16.5px;
    line-height: 19px;
    color: var(--navy);
  }
  .letter {
    position: absolute;
    left: 103px;
    top: 306px;
    width: 737px;
    font-size: 17.5px;
    line-height: 20.5px;
  }
  .letter-date { margin-bottom: 23px; }
  .letter-recipient { margin-bottom: 20px; }
  .letter-body p { text-align: justify; }
  .letter-closing { margin-top: 20px; }
  .letter-signature { margin-top: 20px; }
</style>
</head>
<body>
  <main class="letterhead">
    <svg class="header-curve" viewBox="0 0 936 260" aria-hidden="true">
      <path d="M-10,178 Q380,312 946,82" fill="none" stroke="var(--navy)" stroke-width="11"/>
    </svg>

    <div class="brand-mark" aria-hidden="true"></div>
    <div class="brand-name">Tall Oak Circle</div>
    <address class="brand-contact" style="font-style: normal;">
      215 Maple Row Fairhaven, Vermont, 05743<br>
      555-014-2290 ext 23
    </address>

    <article class="letter">
      <p class="letter-date">April 28. 2014</p>
      <p class="letter-recipient">Alex Carter,<br>1234 Street Ave,<br>Somewhere.</p>
      <div class="letter-body">
        <p>Dear Ms Carter,</p>
        <p>Lorem ipsum dolor sit amet, consectetur adipiscing elit. Vestibulum sollicitudin rhoncus molestie. Etiam sed libero ultricies, cursus nisl at, scelerisque diam. Aliquam erat volutpat. Phasellus vel dignissim eros. Nullam eu lorem fermentum, porta magna a, sodales massa. Lorem ipsum dolor sit amet, consectetur adipiscing elit. Duis mollis, tortor sit amet mattis suscipit, nulla quam dictum enim, at maximus sapien ante vitae massa. Maecenas molestie neque vel purus fringilla, id consectetur sapien volutpat. Sed imperdiet bibendum tellus, a feugiat diam finibus nec.</p>
        <p>Lorem ipsum dolor sit amet, consectetur adipiscing elit. Pellentesque blandit quam vitae nibh mattis, in euismod mi tempor. Aenean pulvinar scelerisque turpis, fermentum pharetra arcu commodo quis. Donec vitae orci pulvinar, faucibus felis id, gravida dolor. Morbi at faucibus ante, dictum varius elit. Nulla purus eros, cursus sit amet scelerisque a, condimentum aliquam est. Nulla sed nulla sagittis, tempor massa non, volutpat libero. Quisque sed semper elit, vitae mattis dolor. Fusce tellus orci, mattis eu orci sed, facilisis sollicitudin velit. In porttitor lectus velit, eget auctor augue euismod quis. Suspendisse in libero ut nunc ultricies posuere non ac ipsum. Fusce consequat elementum turpis, eu feugiat purus molestie lacinia.</p>
      </div>
      <p class="letter-closing">Sincerely</p>
      <p class="letter-signature">Mr.Carter</p>
    </article>
  </main>
</body>
</html>
```